Verdant Medispa Business Card

need a business card for our medispa, attached please see the logo.
our website is https://verdantmedispa-example.com

Sorina Belcourt, MD
Internal Medicine

555-204-7193

Sorina@verdantmedispa-example.com

Www.Verdantmedispa-example.com

738 E Harlow Blvd N, Ste 512, Katy, TX 77981

Target Market(s)

MedSpa, Cosmetics, Esthetics

Industry/Entity Type

MedicalSpa

Contact Information for Business Card

Please see the attached business card which i pulled from the internet. I like the idea back as a logo and front with info.

Font styles to use
Decorative

Requirements
Must have
• Color should be matching with Logo and Website theme, Also I like to have QR code for the website

```html
<!DOCTYPE html>
<html lang="en">
<head>
<meta charset="UTF-8">
<title>Verdant Medispa Business Card</title>
<link rel="stylesheet" href="https://fonts.googleapis.com/css2?family=Cinzel+Decorative:wght@400&family=Poppins:wght@300;400;500&display=swap">
<style>
  :root {
    --backdrop: #d9d9d9;
    --backdrop-edge: #bdbdbd;
    --card-brown: #7b6654;
    --card-white: #ffffff;
    --gold: #c9a227;
    --ink: #2b2b2b;
    --ink-soft: #444444;
    --rule: #9a9a9a;
    --ghost: #f0f0f0;
    --qr-fill: #e9e4d8;
  }
  * { margin: 0; padding: 0; box-sizing: border-box; }
  html, body { width: 1200px; height: 852px; overflow: hidden; }
  body {
    background: radial-gradient(ellipse at center, var(--backdrop) 55%, var(--backdrop-edge) 100%);
    font-family: "Poppins", sans-serif;
    position: relative;
  }
  .card {
    position: absolute;
    top: 271px;
    width: 540px;
    height: 309px;
    border-radius: 16px;
    overflow: hidden;
    box-shadow: 0 6px 18px rgba(0,0,0,0.22);
  }
  .card--back {
    left: 40px;
    background: var(--card-brown);
    display: flex;
    align-items: center;
    justify-content: center;
  }
  .card--front {
    left: 620px;
    background: var(--card-white);
    border-bottom: 7px solid var(--gold);
  }
  .brand-name {
    font-family: "Cinzel Decorative", serif;
    color: var(--gold);
    font-weight: 400;
    white-space: nowrap;
  }
  .card--back .brand-name { font-size: 36px; }
  .card--front .brand-name {
    position: absolute;
    left: 30px;
    top: 46px;
    font-size: 26px;
  }
  .brand-ghost {
    position: absolute;
    right: 40px;
    top: 18px;
    width: 110px;
    height: 110px;
    border-radius: 50%;
    background: var(--ghost);
  }
  .address {
    position: absolute;
    right: 30px;
    top: 100px;
    text-align: right;
    font-style: normal;
    font-size: 12px;
    line-height: 18px;
    color: var(--ink);
  }
  .rule { position: absolute; height: 1px; background: var(--rule); }
  .rule--top { left: 30px; right: 30px; top: 144px; }
  .rule--mid { left: 30px; width: 230px; top: 206px; }
  .person { position: absolute; left: 30px; top: 154px; }
  .person__name { font-size: 18px; font-weight: 400; color: var(--ink); line-height: 24px; }
  .person__title { font-size: 13px; font-weight: 400; color: var(--gold); line-height: 20px; }
  .contacts { position: absolute; left: 30px; top: 216px; list-style: none; }
  .contacts li {
    display: flex;
    align-items: center;
    gap: 9px;
    font-size: 12px;
    line-height: 24px;
    color: var(--ink-soft);
  }
  .contacts svg { width: 12px; height: 12px; flex: none; }
  .qr-code {
    position: absolute;
    right: 30px;
    top: 170px;
    width: 78px;
    height: 78px;
    border: 2px solid var(--gold);
    border-radius: 4px;
    background: var(--qr-fill);
  }
</style>
</head>
<body>
  <section class="card card--back" aria-label="Card back">
    <span class="brand-name">Verdant Medispa</span>
  </section>

  <section class="card card--front" aria-label="Card front">
    <span class="brand-ghost" aria-hidden="true"></span>
    <span class="brand-name">Verdant Medispa</span>

    <address class="address">
      738 E Harlow Blvd N, Ste 512<br>
      Katy, TX 77981
    </address>

    <div class="rule rule--top"></div>

    <div class="person">
      <p class="person__name">Sorina Belcourt, MD</p>
      <p class="person__title">Internal Medicine</p>
    </div>

    <div class="rule rule--mid"></div>

    <ul class="contacts">
      <li>
        <svg viewBox="0 0 24 24" aria-hidden="true"><path fill="#c9a227" d="M6.6 10.8a15 15 0 0 0 6.6 6.6l2.2-2.2a1 1 0 0 1 1-.25 11.4 11.4 0 0 0 3.6.57 1 1 0 0 1 1 1V20a1 1 0 0 1-1 1A17 17 0 0 1 3 4a1 1 0 0 1 1-1h3.5a1 1 0 0 1 1 1c0 1.25.2 2.45.57 3.57a1 1 0 0 1-.25 1z"/></svg>
        555-204-7193
      </li>
      <li>
        <svg viewBox="0 0 24 24" aria-hidden="true"><rect x="2" y="5" width="20" height="14" rx="2" fill="#c9a227"/><path d="M3 6l9 7 9-7" fill="none" stroke="#fff" stroke-width="1.6"/></svg>
        Sorina@verdantmedispa-example.com
      </li>
      <li>
        <svg viewBox="0 0 24 24" aria-hidden="true"><circle cx="12" cy="12" r="10" fill="#c9a227"/><path d="M2 12h20M12 2c3 3 3 17 0 20M12 2c-3 3-3 17 0 20" fill="none" stroke="#fff" stroke-width="1.4"/></svg>
        Www.Verdantmedispa-example.com
      </li>
    </ul>

    <div class="qr-code" role="img" aria-label="QR code linking to the website"></div>
  </section>
</body>
</html>
```